Website 950x200 Header w/ logo

I'm in need of a website header for a new site called DaysofMarco.com

The site is basically a glorified blog for myself to write my thoughts about politics, sports, TV shows, current events, whatever. I have a lot of interests.

The site is going to look very very similar to http://www.quickmakerhub.example/4937261/6-tips-to-hold-the-lead-in-design-work

but instead of having a dynamic header that becomes the picture with each article, its just going to be a static header in which I'd like to have the name of the site (Days of Marco) and some kind of logo, pictures, etc - I'm totally open to anything. The only thing is it needs to have a dark (probably black) background and needs to be 950x200px.

I envision a black background, with gray and white as the primary colors and then some secondary colors potentially, but again I'm open to anything as long as it's on the black background or some kind of charcoal gray or wahtever. On the site the black part will go all the way from the left of the screen to the right no matter what the window size, but I'd like to keep all the content inside of 950x200px

email me marco.pellwin@mailnest.example if you have any questions. Thanks!

Industry/Entity Type

Tv

```html
<!DOCTYPE html>
<html lang="en">
<head>
<meta charset="utf-8">
<title>Days of Marco — 8 Ways to Win the Race for Creative Talent</title>
<link rel="stylesheet" href="https://fonts.googleapis.com/css2?family=Bebas+Neue&family=Open+Sans:wght@400;600&family=Roboto+Slab:wght@700;800&display=swap">
<style>
  :root {
    --stage: #ededed;
    --ink: #111111;
    --black: #000000;
    --white: #ffffff;
    --nav-grey: #9a9a9a;
    --rule: #2b2b2b;
    --rule-light: #cfcfcf;
    --body: #4a4a4a;
    --muted: #9b9b9b;
    --link-blue: #1ea2d8;
    --date-green: #34d26a;
    --tile-blank: #eeeeee;
    --font-head: "Bebas Neue", "Arial Narrow", sans-serif;
    --font-body: "Open Sans", Arial, sans-serif;
    --font-slab: "Roboto Slab", Georgia, serif;
  }
  * { box-sizing: border-box; margin: 0; padding: 0; }
  html, body { width: 1200px; height: 900px; overflow: hidden; background: var(--stage); }
  .page {
    position: absolute; left: 37px; top: 13px;
    width: 751px; height: 583px;
    transform: scale(1.5); transform-origin: top left;
    background: var(--white); overflow: hidden;
    font-family: var(--font-body); color: var(--body);
  }
  /* top navigation */
  .topbar {
    height: 30px; background: var(--black);
    display: flex; align-items: center; justify-content: space-between;
    padding: 0 20px 0 32px;
    font-family: var(--font-slab); font-weight: 800; font-size: 10.5px;
  }
  .sections { display: flex; list-style: none; }
  .sections li { color: var(--nav-grey); padding: 0 10px; border-left: 1px solid #555; line-height: 14px; }
  .sections li:first-child { color: var(--white); padding-left: 0; border-left: none; }
  .utility { display: flex; align-items: center; font-family: var(--font-body); font-weight: 600; font-size: 9.5px; letter-spacing: .8px; color: var(--nav-grey); }
  .utility span { padding: 0 9px; line-height: 12px; }
  .utility span + span { border-left: 1px solid #555; }
  .utility svg { margin-left: 8px; }
  /* masthead */
  .masthead {
    height: 153px; background: linear-gradient(180deg, #0d0d0d 0%, #050505 60%, #000 100%);
    padding: 52px 0 0 32px;
  }
  .wordmark {
    font-family: var(--font-head); color: var(--white);
    font-size: 58px; line-height: 48px; letter-spacing: 1px;
  }
  /* content */
  .content { display: flex; height: 400px; }
  .article { width: 486px; border-right: 1px solid var(--rule-light); position: relative; padding: 12px 0 0 30px; }
  .article-band {
    position: absolute; left: 0; top: 0; width: 280px; height: 36px;
    background: linear-gradient(90deg, #e6e6e6 0%, rgba(255,255,255,0) 100%);
  }
  .headline { position: relative; font-family: var(--font-head); color: var(--ink); font-size: 35px; line-height: 31px; font-weight: 400; letter-spacing: -.3px; }
  .byline { margin-top: 12px; font-family: var(--font-head); font-size: 17px; color: var(--link-blue); }
  .byline small { font-family: var(--font-slab); font-size: 8px; font-weight: 700; color: var(--muted); margin-right: 2px; }
  .dek { margin-top: 8px; width: 390px; font-size: 9.8px; line-height: 14px; color: var(--ink); }
  .share {
    margin-top: 15px; width: 375px; height: 40px;
    border-top: 1px solid var(--rule); border-bottom: 1px solid var(--rule);
    display: flex; align-items: center; gap: 11px;
  }
  .share-dot { position: relative; width: 17px; height: 17px; border-radius: 50%; background: var(--ink); }
  .share-dot sup { position: absolute; left: 13px; top: -7px; font-size: 7px; font-weight: 600; color: var(--ink); }
  .body-copy { margin-top: 14px; width: 378px; font-size: 10.5px; line-height: 17px; color: var(--body); }
  .body-copy p + p { margin-top: 6px; }
  /* sidebar */
  .sidebar { width: 265px; padding: 20px 25px 0 18px; }
  .label {
    font-family: var(--font-slab); font-weight: 800; font-size: 9px; color: var(--ink);
    letter-spacing: .3px;
  }
  .archives-title { border-top: 1px solid var(--rule); border-bottom: 1px solid var(--rule-light); padding: 4px 0 3px; }
  .weekdays { display: grid; grid-template-columns: repeat(5, 40.5px); margin-top: 4px; font-family: var(--font-head); font-size: 11px; color: var(--muted); }
  .archive-grid { position: relative; display: grid; grid-template-columns: repeat(5, 40px); grid-auto-rows: 40px; gap: 1px; margin-top: 2px; }
  .tile { display: block; }
  .tile-blank { background: var(--tile-blank); font-family: var(--font-head); font-size: 28px; color: var(--white); text-align: center; line-height: 42px; }
  .archive-next { position: absolute; left: 207px; top: 108px; }
  .tags { margin-top: 10px; border-top: 1px solid var(--rule-light); padding: 12px 0 18px; font-family: var(--font-slab); font-weight: 700; font-size: 8px; color: var(--muted); border-bottom: 1px solid var(--rule); }
  .editor { padding-top: 14px; }
  .editor-name { font-family: var(--font-head); font-size: 17px; color: var(--muted); margin-top: 2px; padding-bottom: 14px; border-bottom: 1px solid var(--rule); }
  .date { padding-top: 7px; }
  .date-box { margin-top: 4px; background: var(--black); height: 40px; display: flex; padding: 5px 8px; gap: 12px; }
  .date-box strong { font-family: var(--font-head); font-weight: 400; font-size: 26px; color: var(--white); line-height: 26px; }
  .date-box span { font-family: var(--font-head); font-size: 12px; line-height: 12px; color: var(--date-green); }
</style>
</head>
<body>
<div class="page">
  <nav class="topbar">
    <ul class="sections">
      <li>Qm.MAKE</li><li>Qm.LIVE</li><li>Qm.FORM</li><li>Qm.TEST</li>
    </ul>
    <div class="utility">
      <span>SUBSCRIBE</span><span>CREATE DAILY</span>
      <svg width="14" height="14" viewBox="0 0 14 14"><circle cx="5.5" cy="5.5" r="4" fill="none" stroke="#9a9a9a" stroke-width="2"/><line x1="8.5" y1="8.5" x2="13" y2="13" stroke="#9a9a9a" stroke-width="2.5"/></svg>
      <svg width="13" height="13" viewBox="0 0 13 13"><circle cx="2" cy="11" r="2" fill="#9a9a9a"/><path d="M1 6a6 6 0 0 1 6 6M1 1a11 11 0 0 1 11 11" fill="none" stroke="#9a9a9a" stroke-width="2"/></svg>
      <svg width="13" height="13" viewBox="0 0 13 13"><circle cx="10.5" cy="2.5" r="2.2" fill="#9a9a9a"/><circle cx="2.5" cy="6.5" r="2.2" fill="#9a9a9a"/><circle cx="10.5" cy="10.5" r="2.2" fill="#9a9a9a"/><path d="M10.5 2.5 2.5 6.5 10.5 10.5" fill="none" stroke="#9a9a9a" stroke-width="1.5"/></svg>
    </div>
  </nav>

  <header class="masthead">
    <h1 class="wordmark">DAYS OF<br>MARCO</h1>
  </header>

  <div class="content">
    <article class="article">
      <div class="article-band" role="img" aria-label="Light grey diagonal stripe band"></div>
      <h2 class="headline">8 WAYS TO WIN THE RACE FOR<br>CREATIVE TALENT</h2>
      <p class="byline"><small>BY:</small> NOLAN REEVE</p>
      <p class="dek">The Brightwell's Nolan Reeve talks about what, beyond a paycheck, companies can offer to attract and motivate creative talent.</p>
      <div class="share">
        <svg width="17" height="17" viewBox="0 0 17 17"><path d="M8.5 1.5a7 6.3 0 1 1-3.6 11.7L1.8 15l1.1-3.2A7 6.3 0 0 1 8.5 1.5z" fill="none" stroke="#111" stroke-width="1.6"/></svg>
        <svg width="17" height="17" viewBox="0 0 17 17"><circle cx="8.5" cy="8.5" r="8.5" fill="#111"/><path d="M8.5 4.5v8M4.5 8.5h8" stroke="#fff" stroke-width="1.8"/></svg>
        <span class="share-dot"></span>
        <span class="share-dot"></span>
        <span class="share-dot"><sup>227</sup></span>
        <span class="share-dot"><sup>92</sup></span>
      </div>
      <div class="body-copy">
        <p>Many creative businesses limit their talent recruitment and retention strategies to money and flattery.</p>
        <p>But companies adept at unlocking what I describe as Profitable Creativity are built on more sustainable practices. Many of these, I learned first hand over a decade building a company filled with demanding, world-class talent. In that time, we lost not one of our artists to a competitor. The others I've experienced in my work as a confidant to some of the world's most successful chief creative officers and company owners. In all, there are eight practices. And seven come with the added benefit that they cost nothing to implement.</p>
      </div>
    </article>

    <aside class="sidebar">
      <h3 class="label archives-title">THE ARCHIVES</h3>
      <div class="weekdays"><span>MON</span><span>TUE</span><span>WED</span><span>THUR</span><span>FRI</span></div>
      <div class="archive-grid">
        <span class="tile" style="background:#2f5a3a" role="img" aria-label="Article thumbnail photo"></span>
        <span class="tile" style="background:#a5845a" role="img" aria-label="Article thumbnail photo"></span>
        <span class="tile tile-blank">27</span>
        <span class="tile tile-blank">28</span>
        <span class="tile tile-blank">29</span>
        <span class="tile" style="background:#b9a98c" role="img" aria-label="Article thumbnail photo"></span>
        <span class="tile" style="background:#4d5660" role="img" aria-label="Article thumbnail photo"></span>
        <span class="tile" style="background:#8a5a3c" role="img" aria-label="Article thumbnail photo"></span>
        <span class="tile" style="background:#c8497e" role="img" aria-label="Article thumbnail photo"></span>
        <span class="tile" style="background:#c07a3a" role="img" aria-label="Article thumbnail photo"></span>
        <span class="tile" style="background:#3a3f55" role="img" aria-label="Article thumbnail photo"></span>
        <span class="tile" style="background:#b78f55" role="img" aria-label="Article thumbnail photo"></span>
        <span class="tile" style="background:#7c6d8a" role="img" aria-label="Article thumbnail photo"></span>
        <span class="tile" style="background:#6b7a58" role="img" aria-label="Article thumbnail photo"></span>
        <span class="tile" style="background:#4f6470" role="img" aria-label="Article thumbnail photo"></span>
        <span class="tile" style="background:#c6ccd2" role="img" aria-label="Article thumbnail photo"></span>
        <span class="tile" style="background:#5a6fa0" role="img" aria-label="Article thumbnail photo"></span>
        <span class="tile" style="background:#8aa36a" role="img" aria-label="Article thumbnail photo"></span>
        <span class="tile" style="background:#c4a070" role="img" aria-label="Article thumbnail photo"></span>
        <span class="tile" style="background:#6a8a5a" role="img" aria-label="Article thumbnail photo"></span>
        <svg class="archive-next" width="10" height="12" viewBox="0 0 10 12"><path d="M2 1l6 5-6 5" fill="none" stroke="#9a9a9a" stroke-width="2.2"/></svg>
      </div>
      <p class="tags">CREATIVITY \ CULTURE \ COMMERCE</p>
      <div class="editor">
        <h3 class="label">EDITOR:</h3>
        <p class="editor-name">MARA QUILLEN</p>
      </div>
      <div class="date">
        <h3 class="label">DATE</h3>
        <div class="date-box"><strong>03 / 14</strong><span>TWO THOUSAND AND<br>THIRTEEN</span></div>
      </div>
    </aside>
  </div>
</div>
</body>
</html>
```